Redesign Local Plumber Website

redesign of existing plumbing website

Mobile Responsive
Professional
modern
easy enquiry
Map embed

Please see existing site for text and images. Please feel free to suggest improvements and any additional features
letmefixyourtaps.com.au

attached is logo and the Australian owned badge which we also want featuring

Target Market(s)

Plumbing & Gas Services

Industry/Entity Type

Plumbing

Font styles to use
Sans Serif

Requirements
Must have
• existing logo
Nice to have
• new design
Should not have
• same design

```html
<!DOCTYPE html>
<html lang="en">
<head>
<meta charset="utf-8">
<title>Let Me Fix Your Taps – Plumbing, Heating &amp; Air Conditioning</title>
<link rel="stylesheet" href="https://fonts.googleapis.com/css2?family=Roboto:wght@300;400;500;700;900&display=swap">
<style>
:root{
  --blue:#1b87d0;
  --blue-bright:#1e9be0;
  --navy:#1f3a5f;
  --navy-deep:#172f4f;
  --ink:#222b36;
  --text:#5c6670;
  --muted:#8a939c;
  --pale:#e8e9ef;
  --line:#e3e5ea;
  --gold:#f5b90f;
  --white:#ffffff;
}
*{box-sizing:border-box;margin:0;padding:0}
html,body{width:1200px;height:4206px;overflow:hidden}
body{font-family:"Roboto",Arial,sans-serif;color:var(--ink);background:var(--white);position:relative}
.abs{position:absolute}
a{color:inherit;text-decoration:none}
svg{display:block}

/* top bar */
.topbar{top:0;left:0;width:1200px;height:23px;background:var(--blue);color:#fff;font-size:9px;font-weight:500}
.topbar .links{left:154px;top:6px}
.topbar .status{right:150px;top:6px;white-space:nowrap}
.topbar .social{right:60px;top:6px;display:flex;gap:12px}
.topbar .social span{width:11px;height:11px;border-radius:2px;background:rgba(255,255,255,.85)}

/* header */
.header{top:23px;left:0;width:1200px;height:75px;background:#fff}
.brand{left:155px;top:16px;display:flex;align-items:center;gap:10px}
.brand .dot{width:34px;height:34px;border-radius:50%;background:var(--navy)}
.brand .name{font-size:20px;font-weight:700;color:var(--blue);letter-spacing:.5px;text-transform:uppercase}
.contact{display:flex;gap:12px;align-items:center;top:24px}
.contact .ic{width:30px;height:26px;border-radius:4px;display:flex;align-items:center;justify-content:center}
.contact b{display:block;font-size:11px;font-weight:500;color:var(--ink)}
.contact small{font-size:10px;color:var(--muted)}

/* nav */
.nav{top:98px;left:0;width:1200px;height:54px;border-top:1px solid var(--line);border-bottom:1px solid var(--line);background:#fff}
.nav ul{list-style:none;display:flex;gap:24px;position:absolute;left:156px;top:19px;font-size:12px;color:#555}
.nav li.active{color:var(--blue)}
.btn{display:inline-flex;align-items:center;justify-content:center;background:var(--blue);color:#fff;font-weight:700;font-size:12px;text-transform:uppercase;border-radius:3px}
.nav .btn{position:absolute;right:168px;top:13px;width:139px;height:28px}

/* hero */
.hero{top:152px;left:0;width:1200px;height:464px;background:linear-gradient(100deg,#e9eef2 0%,#cfd7de 45%,#6f8aa8 70%,#2f4f7a 100%)}
.hero h1{position:absolute;left:168px;top:80px;font-size:33px;line-height:39px;font-weight:700;color:var(--navy-deep);text-transform:uppercase}
.hero p{position:absolute;left:170px;top:170px;font-size:13px;color:#44505c}
.hero .btn{position:absolute;left:170px;top:220px;width:171px;height:38px}
.zipband{left:137px;top:524px;width:916px;height:92px}
.zipband .txt{position:absolute;left:163px;top:24px;color:#fff;font-size:18px;font-weight:700;line-height:22px;text-transform:uppercase}
.zipband .field{position:absolute;left:449px;top:27px;width:399px;height:38px;background:#fff;border-radius:19px;font-size:13px;color:#555;padding:11px 0 0 33px}
.zipband .field .go{position:absolute;right:0;top:0;width:163px;height:38px;border-radius:19px;background:var(--navy-deep);color:#fff;font-weight:700;font-size:13px;display:flex;align-items:center;justify-content:center}

/* we fix */
.fix h2{position:absolute;left:178px;top:682px;font-size:26px;line-height:32px;font-weight:700;color:var(--navy-deep);text-transform:uppercase}
.fix .bar{left:155px;top:688px;width:4px;height:34px;background:var(--gold)}
.fix p{position:absolute;left:180px;top:752px;width:320px;font-size:11px;line-height:14.5px;color:var(--muted)}
.fix .btn{position:absolute;left:182px;top:874px;width:104px;height:31px;background:var(--navy-deep);font-size:11px;text-transform:none;font-weight:500}
.fix .panel{left:544px;top:674px;width:490px;height:188px;background:linear-gradient(120deg,#3c4a5a,#1e2a38);border-radius:14px}
.hexcard{position:absolute;width:131px;height:131px;background:#fff;box-shadow:0 4px 14px rgba(0,0,0,.15);clip-path:polygon(50% 0,100% 14%,100% 100%,0 100%,0 14%);text-align:center;font-size:11px;font-weight:500;color:#444;text-transform:uppercase;padding-top:78px;line-height:13px}
.hexcard svg{position:absolute;left:45px;top:28px}
.hexcard.offer{background:var(--blue-bright);color:#fff;text-transform:none;padding-top:30px}
.hexcard.offer b{display:block;font-size:23px;line-height:28px;font-weight:500}
.hexcard.offer small{display:block;font-size:9px;line-height:11px;margin-top:4px}
.hexcard.offer span{display:inline-block;margin-top:6px;background:#fff;color:var(--blue);font-size:9px;border-radius:10px;padding:3px 12px}

/* services band */
.svcband{top:968px;left:0;width:1200px;height:343px;background:linear-gradient(90deg,#c5ced8 0%,#8d9db0 40%,#5d7ea6 60%,#4f7cb3 100%)}
.svcband .photo{position:absolute;left:0;top:0;width:650px;height:343px;background:linear-gradient(90deg,#b9c3cc,#7f8e9d 60%,rgba(90,125,170,0))}
.svcband h2{position:absolute;left:668px;top:76px;color:#fff;font-size:25px;font-weight:700;text-transform:uppercase}
.svcband p{position:absolute;left:668px;top:118px;width:370px;color:#fff;font-size:13px;line-height:16px}
.svcband .btn{position:absolute;left:668px;top:224px;width:200px;height:38px;background:var(--blue-bright)}

/* why choose */
.why{top:1311px;left:0;width:1200px;height:510px;background:var(--pale)}
.why h2{position:absolute;width:100%;top:53px;text-align:center;font-size:26px;font-weight:700;color:var(--navy-deep);text-transform:uppercase}
.why .sub{position:absolute;width:100%;top:95px;text-align:center;font-size:12px;color:var(--text)}
.feat{position:absolute;width:147px;height:130px;background:#fff;border-radius:6px;box-shadow:0 3px 10px rgba(0,0,0,.08);clip-path:polygon(0 0,100% 0,100% 88%,50% 100%,0 88%);text-align:center;font-size:11px;line-height:14px;color:#333;padding-top:78px}
.feat svg{position:absolute;left:50%;margin-left:-24px;top:22px}

/* reviews */
.reviews{top:1821px;left:0;width:1200px;height:526px;background:linear-gradient(135deg,#2a4c78,#1f3d66 60%,#1b3558)}
.reviews h2{position:absolute;width:100%;top:56px;text-align:center;color:#fff;font-size:26px;font-weight:700;text-transform:uppercase}
.stat{position:absolute;top:130px;width:200px;text-align:center;color:#fff}
.stat svg{margin:0 auto}
.stat .lbl{font-size:12px;margin-top:16px;text-transform:uppercase}
.stat .num{font-size:37px;margin-top:6px}
.stat .stars{color:var(--gold);font-size:14px;letter-spacing:2px}
.reviews .rating{position:absolute;width:100%;top:354px;text-align:center;color:#fff;font-size:11px}
.reviews .rating u{text-decoration:underline}
.reviews .rating .gold{color:var(--gold)}

.testi{position:absolute;top:2270px;width:250px;text-align:center}
.testi .avatar{width:146px;height:146px;border-radius:50%;border:4px solid #fff;box-shadow:0 2px 8px rgba(0,0,0,.2);margin:0 auto;background:radial-gradient(circle at 50% 40%,#d7c0ad,#8a7a70 70%,#5a6f88)}
.testi p{margin-top:30px;font-size:11px;line-height:18px;color:#444}
.testi b{display:block;margin-top:14px;font-size:13px;font-weight:700;text-transform:uppercase}
.testi small{font-size:10px;color:#666}

/* gallery */
.sechead{position:absolute;left:155px;font-size:22px;font-weight:700;color:var(--navy-deep);text-transform:uppercase;padding-left:18px;border-left:4px solid var(--blue)}
.arrowbtn{position:absolute;width:30px;height:30px;border-radius:50%;display:flex;align-items:center;justify-content:center}
.tile{position:absolute;top:2735px;width:235px;height:270px}
.tile.hover{background:var(--navy)}
.tile.hover b{position:absolute;left:28px;top:208px;color:var(--blue-bright);font-size:14px}
.tile.hover small{position:absolute;left:28px;top:230px;color:#fff;font-size:10px}

/* tips */
.tips h2{position:absolute;width:100%;top:3050px;text-align:center;font-size:22px;font-weight:700;color:var(--ink);text-transform:uppercase}
.tip{position:absolute;top:3117px;width:281px;height:253px}
.tip .img{position:absolute;left:0;top:0;width:281px;height:182px}
.tip .card{position:absolute;left:19px;top:121px;width:242px;height:100px;background:#fff;text-align:center;font-size:14px;line-height:18px;color:#222;padding-top:34px}
.tip .btn{position:absolute;left:19px;top:221px;width:242px;height:30px;border-radius:0;text-transform:none;font-weight:400;font-size:12px}

/* cta + footer */
.cta{top:3442px;left:0;width:1200px;height:764px;background:linear-gradient(100deg,#f2f4f6 0%,#e3e7ec 45%,#a9b7c7 65%,#5d7493 100%)}
.cta h2{position:absolute;left:150px;top:94px;font-size:23px;font-weight:700;color:var(--navy-deep);text-transform:uppercase}
.cta p{position:absolute;left:153px;top:130px;font-size:12px;line-height:19px;color:#555}
.cta .btn{position:absolute;left:153px;top:179px;width:236px;height:39px;font-size:13px}
.footer-shape{left:0;top:3732px}
.footer{color:#fff}
.addr{position:absolute;top:3854px;font-size:10px;line-height:14px}
.addr b{display:block;font-size:10px;font-weight:700;margin-bottom:10px}
.addr .tel{margin-top:10px;display:flex;gap:6px;align-items:center}
.fsocial{position:absolute;left:903px;top:3866px;display:flex;gap:7px}
.fsocial span{width:26px;height:26px;border:1.5px solid #fff}
.badge{left:965px;top:3910px;width:68px;height:68px;border-radius:50%;background:#2e8a3e;border:4px solid #fff}
.fcol{position:absolute;top:3986px;font-size:12px;line-height:22px}
.fcol h4{font-size:10px;font-weight:700;margin-bottom:14px}
.fcol.small{font-size:10px}
.news{position:absolute;left:601px;top:3986px;width:432px}
.news h4{font-size:10px;font-weight:700}
.news p{font-size:10px;line-height:22px;margin-top:16px;color:#e0e6ee}
.news .form{display:flex;gap:6px;margin-top:12px}
.news .input{width:325px;height:36px;background:#fff;color:#555;font-size:10px;padding:12px 0 0 20px}
.news .submit{width:99px;height:36px;background:var(--blue-bright);font-size:11px;display:flex;align-items:center;justify-content:center}
.copy{left:603px;top:4130px;font-size:9px;font-weight:500}
</style>
</head>
<body>

<!-- top bar -->
<div class="abs topbar">
  <div class="abs links">Quick Services &nbsp;|&nbsp; Read Our Reviews &nbsp;|&nbsp; Life Time Support</div>
  <div class="abs status">It's Monday, 1:01 PM &amp; We're Always Open &nbsp;|&nbsp; Follow us</div>
  <div class="abs social"><span></span><span></span><span></span><span></span></div>
</div>

<!-- header -->
<header class="abs header">
  <div class="abs brand"><span class="dot"></span><span class="name">Let Me Fix Your Taps</span></div>
  <div class="abs contact" style="left:640px">
    <div class="ic" style="background:var(--blue)">
      <svg width="12" height="16" viewBox="0 0 12 16"><path d="M6 0a6 6 0 0 0-6 6c0 4.5 6 10 6 10s6-5.5 6-10a6 6 0 0 0-6-6zm0 8.5A2.5 2.5 0 1 1 6 3.5a2.5 2.5 0 0 1 0 5z" fill="#fff"/></svg>
    </div>
    <div><b>Plumber Services</b><small>48 Harbour Rd. Eastvale, NSW 2140</small></div>
  </div>
  <div class="abs contact" style="left:920px">
    <div class="ic" style="background:var(--navy-deep)">
      <svg width="14" height="14" viewBox="0 0 24 24"><path d="M6.6 10.8a15 15 0 0 0 6.6 6.6l2.2-2.2a1 1 0 0 1 1-.25 11.4 11.4 0 0 0 3.6.57 1 1 0 0 1 1 1V20a1 1 0 0 1-1 1A17 17 0 0 1 3 4a1 1 0 0 1 1-1h3.5a1 1 0 0 1 1 1c0 1.25.2 2.45.57 3.57a1 1 0 0 1-.25 1z" fill="#fff"/></svg>
    </div>
    <div><b>Call Us Today</b><small>000 000 0000</small></div>
  </div>
</header>

<!-- nav -->
<nav class="abs nav">
  <ul>
    <li class="active">Home</li><li>Why Us?</li><li>Air Conditioning</li><li>Heating</li><li>Plumbing</li><li>Water Treatment</li><li>Contact Us</li>
  </ul>
  <a class="btn">Shedule Service</a>
</nav>

<!-- hero -->
<section class="abs hero" role="img" aria-label="Kitchen sink with a smiling plumber holding hoses and a tool bag">
  <h1>Comfort Is On The<br>Plumber Services</h1>
  <p>Your Air Conditioning, Heating And Plumbing Experts</p>
  <a class="btn">Get Started Now</a>
</section>
<div class="abs zipband">
  <svg class="abs" style="left:0;top:0" width="916" height="92" viewBox="0 0 916 92"><path d="M28 0H884l32 92H0z" fill="#1b87d0"/></svg>
  <svg class="abs" style="left:100px;top:26px" width="40" height="44" viewBox="0 0 40 44"><path d="M4 2h20v40H4z" fill="none" stroke="#163a64" stroke-width="3"/><path d="M4 2l16 6v36L4 42z" fill="#163a64"/><circle cx="16" cy="24" r="1.8" fill="#fff"/></svg>
  <div class="txt">Get Us To Your<br>Front Door Today</div>
  <div class="field">Enter Your Zip Code<span class="go">GET STARTED</span></div>
</div>

<!-- we fix -->
<section class="fix">
  <div class="abs bar"></div>
  <h2>We Fix Your<br>Plumbing Problems</h2>
  <p>Lorem Ipsum is simply dummy text of the printing and typesetting industry. Lorem Ipsum has been the industry's standard dummy text ever since the 1500s, when an unknown printer took a galley of type and scrambled it to make a type specimen book. It has survived not only five centuries, but also the leap into electronic typesetting, remaining essentially unchanged.</p>
  <a class="btn">About Us</a>
  <div class="abs panel"></div>
  <div class="hexcard" style="left:596px;top:776px">
    <svg width="42" height="42" viewBox="0 0 42 42"><path d="M8 34a13 13 0 0 1 26 0z" fill="#f5b90f"/><rect x="5" y="34" width="32" height="4" fill="#d9dde2"/><path d="M21 4v8M6 12l5 5M36 12l-5 5" stroke="#f5b90f" stroke-width="2.5"/></svg>
    Emergency<br>Services
  </div>
  <div class="hexcard" style="left:735px;top:776px">
    <svg width="42" height="42" viewBox="0 0 42 42"><rect x="8" y="4" width="26" height="34" fill="#fff" stroke="#c9b48a" stroke-width="2"/><path d="M13 13h16M13 19h16M13 25h10" stroke="#c9b48a" stroke-width="2"/><path d="M26 34l10-18" stroke="#f5b90f" stroke-width="3"/></svg>
    Read Our<br>Reviews
  </div>
  <div class="hexcard offer" style="left:874px;top:776px">
    <b>$50 Off</b><small>Any A/c, Heating, Or<br>Plumbing Repair</small><span>See Specials</span>
  </div>
</section>

<!-- plumber services band -->
<section class="abs svcband">
  <div class="photo" role="img" aria-label="Smiling plumber repairing pipes under a sink"></div>
  <h2>Plumber Services</h2>
  <p>From routine maintenance to emergency repairs to quality installation of &nbsp;home comfort systems, Northgate Services works hard all day, every day to ensure that your needs are met and that you and your family can enjoy your home comfortably and worry-free.</p>
  <a class="btn">Request Services Today</a>
</section>

<!-- why choose -->
<section class="abs why">
  <h2>Why Choose Plumber Services</h2>
  <div class="sub">Trusted Professionals for Your Air Conditioning, Heating and Plumbing Needs</div>

  <div class="feat" style="left:232px;top:147px"><svg width="48" height="48" viewBox="0 0 48 48"><circle cx="22" cy="26" r="15" fill="none" stroke="#1f3a5f" stroke-width="2.5"/><path d="M22 17v9l6 4" stroke="#1b87d0" stroke-width="2.5" fill="none"/><path d="M34 6c4 4 6 10 4 16" stroke="#1b87d0" stroke-width="2.5" fill="none"/></svg>On-Time Or it's<br>Free Guarantee</div>
  <div class="feat" style="left:403px;top:147px"><svg width="48" height="48" viewBox="0 0 48 48"><circle cx="22" cy="20" r="14" fill="#1f3a5f"/><text x="22" y="27" text-anchor="middle" font-size="18" font-weight="700" fill="#fff" font-family="Roboto,sans-serif">$</text><path d="M30 30l10 12" stroke="#1b87d0" stroke-width="4"/></svg>No Emergency<br>Charges - EVER</div>
  <div class="feat" style="left:575px;top:147px"><svg width="48" height="48" viewBox="0 0 48 48"><circle cx="24" cy="20" r="15" fill="none" stroke="#1f3a5f" stroke-width="2.5"/><circle cx="24" cy="16" r="4" fill="#1b87d0"/><path d="M16 30c2-6 14-6 16 0" fill="#1b87d0"/><path d="M9 20h30M24 5v30" stroke="#1f3a5f" stroke-width="1.2"/></svg>Locally Owned<br>&amp; Operated</div>
  <div class="feat" style="left:733px;top:147px"><svg width="48" height="48" viewBox="0 0 48 48"><rect x="10" y="6" width="28" height="16" rx="3" fill="none" stroke="#1f3a5f" stroke-width="2"/><path d="M16 26v8M24 26v12M32 26v8" stroke="#1b87d0" stroke-width="2.5"/><circle cx="24" cy="14" r="3" fill="#1b87d0"/></svg>Why Choose<br>Us?</div>

  <div class="feat" style="left:320px;top:284px"><svg width="48" height="48" viewBox="0 0 48 48"><circle cx="24" cy="8" r="5" fill="#1b87d0"/><rect x="10" y="16" width="28" height="5" fill="#1f3a5f"/><path d="M13 24v14M19 24v14M25 24v14M31 24v14M36 24v14" stroke="#1f3a5f" stroke-width="2.5"/><rect x="8" y="40" width="32" height="4" fill="#1f3a5f"/></svg>Industry Leading<br>Warranties</div>
  <div class="feat" style="left:488px;top:284px"><svg width="48" height="48" viewBox="0 0 48 48"><circle cx="26" cy="18" r="14" fill="#1f3a5f"/><text x="26" y="25" text-anchor="middle" font-size="18" font-weight="700" fill="#fff" font-family="Roboto,sans-serif">$</text><path d="M4 38c8-6 16-6 22 0h12" stroke="#1b87d0" stroke-width="3" fill="none"/></svg>No Surprise,<br>Up Front Pricing</div>
  <div class="feat" style="left:654px;top:284px"><svg width="48" height="48" viewBox="0 0 48 48"><path d="M8 4l2 4 4 .5-3 3 .8 4L8 13.5 4.2 15.5l.8-4-3-3 4-.5zM24 2l2 4 4 .5-3 3 .8 4L24 11.5l-3.8 2 .8-4-3-3 4-.5zM40 4l2 4 4 .5-3 3 .8 4L40 13.5l-3.8 2 .8-4-3-3 4-.5z" fill="none" stroke="#1b87d0" stroke-width="1.5"/><circle cx="24" cy="28" r="6" fill="none" stroke="#888" stroke-width="2"/><path d="M12 46c2-8 22-8 24 0" fill="none" stroke="#888" stroke-width="2"/></svg>Highly Trained<br>Technicians</div>
  <div class="feat" style="left:821px;top:284px"><svg width="48" height="48" viewBox="0 0 48 48"><path d="M6 40l18-18M24 22a8 8 0 1 1 8 8" stroke="#c9b48a" stroke-width="3" fill="none"/><path d="M30 40l12-12" stroke="#c9b48a" stroke-width="3"/><circle cx="14" cy="12" r="6" fill="none" stroke="#c9b48a" stroke-width="2"/></svg>Same Day Service &amp;<br>Next Day Installation</div>
</section>

<!-- reviews -->
<section class="abs reviews">
  <h2>What Our Customers Are Saying</h2>
  <div class="stat" style="left:288px">
    <svg width="78" height="62" viewBox="0 0 78 62"><rect x="4" y="2" width="70" height="30" rx="3" fill="#1e9be0"/><path d="M12 12h54M12 20h54" stroke="#1f3d66" stroke-width="3"/><text x="6" y="56" font-size="22" font-weight="900" fill="#1e9be0" font-family="Roboto,sans-serif">$$$</text><path d="M62 38v20M52 48h20M55 41l14 14M69 41L55 55" stroke="#1e9be0" stroke-width="3"/></svg>
    <div class="lbl">Air Conditioning</div><div class="num">29,634</div><div class="stars">★★★★★</div>
  </div>
  <div class="stat" style="left:500px">
    <svg width="78" height="62" viewBox="0 0 78 62"><g fill="none" stroke="#1e9be0" stroke-width="3"><rect x="8" y="4" width="8" height="52" rx="4"/><rect x="20" y="4" width="8" height="52" rx="4"/><rect x="32" y="4" width="8" height="52" rx="4"/><rect x="44" y="4" width="8" height="52" rx="4"/><rect x="56" y="4" width="8" height="52" rx="4"/></g><path d="M2 30h6M64 30h10" stroke="#1e9be0" stroke-width="3"/></svg>
    <div class="lbl">Heating</div><div class="num">40,733</div><div class="stars">★★★★★</div>
  </div>
  <div class="stat" style="left:712px">
    <svg width="78" height="62" viewBox="0 0 78 62"><path d="M14 4v26a20 20 0 0 0 40 0V10h10" fill="none" stroke="#1e9be0" stroke-width="9"/><rect x="6" y="2" width="16" height="6" fill="#1e9be0"/></svg>
    <div class="lbl">Plumbing</div><div class="num">32,125</div><div class="stars">★★★★★</div>
  </div>
  <div class="rating"><b>Plumbing Services | 5.0</b> | Out of 5 Stars &nbsp;| &nbsp;<u>View Reviews</u> &nbsp;| &nbsp;<u class="gold">Write A Review</u></div>
</section>

<div class="testi" style="left:181px">
  <div class="avatar" role="img" aria-label="Customer portrait"></div>
  <p>Lorem Ipsum is simply dummy text of the printing and typesetting industry. Lorem Ipsum has been the industry's standard dummy text ever since the 1500s</p>
  <b>Maya Fenwick</b><small>Lipsum SEO</small>
</div>
<div class="testi" style="left:468px">
  <div class="avatar" role="img" aria-label="Customer portrait"></div>
  <p>Lorem Ipsum is simply dummy text of the printing and typesetting industry. Lorem Ipsum has been the industry's standard dummy text ever since the 1500s</p>
  <b>Tom Hadley</b><small>Lipsum SEO</small>
</div>
<div class="testi" style="left:758px">
  <div class="avatar" role="img" aria-label="Customer portrait"></div>
  <p>Lorem Ipsum is simply dummy text of the printing and typesetting industry. Lorem Ipsum has been the industry's standard dummy text ever since the 1500s</p>
  <b>Leo Barrett</b><small>Lipsum SEO</small>
</div>

<!-- gallery -->
<h2 class="sechead" style="top:2658px">Our Works Gallery</h2>
<div class="arrowbtn" style="left:961px;top:2659px;background:var(--navy-deep)"><svg width="10" height="10" viewBox="0 0 10 10"><path d="M7 1L3 5l4 4" stroke="#fff" stroke-width="1.6" fill="none"/></svg></div>
<div class="arrowbtn" style="left:1002px;top:2659px;background:var(--blue-bright)"><svg width="10" height="10" viewBox="0 0 10 10"><path d="M3 1l4 4-4 4" stroke="#fff" stroke-width="1.6" fill="none"/></svg></div>
<div class="tile" style="left:0;background:linear-gradient(135deg,#8a9099,#d8dcdf 50%,#5b6470)" role="img" aria-label="Chrome U-bend pipe being fitted"></div>
<div class="tile hover" style="left:241px"><b>REPAIR/FIXING</b><small>TANKLESS WATER HEATER</small></div>
<div class="tile" style="left:482px;background:linear-gradient(135deg,#e6e9ec,#9aa6b3 50%,#2f3e52)" role="img" aria-label="Technician servicing a water heater"></div>
<div class="tile" style="left:723px;background:linear-gradient(135deg,#eef0f2,#c7ced6 45%,#3a4a60)" role="img" aria-label="Technician with a clipboard inspecting a unit"></div>
<div class="tile" style="left:965px;background:linear-gradient(135deg,#c3ccd6,#7e93ab 55%,#d0d6dc)" role="img" aria-label="Smiling plumber giving a thumbs up under a sink"></div>

<!-- tips -->
<section class="tips">
  <h2>Expert Tips For You</h2>
  <div class="tip" style="left:155px">
    <div class="img" style="background:linear-gradient(135deg,#c9cfd6,#7c8a9a 55%,#e4e7ea)" role="img" aria-label="Plumber working on pipes"></div>
    <div class="card">Services Sponsors<br>Eastvale Veteran Radiothon</div>
    <a class="btn">Read More</a>
  </div>
  <div class="tip" style="left:454px">
    <div class="img" style="background:linear-gradient(135deg,#eef0f2,#9eb4c8 50%,#2c333b)" role="img" aria-label="Digital thermostat display"></div>
    <div class="card">Top 5 Efficiency Tips for<br>Utility Savings</div>
    <a class="btn">Read More</a>
  </div>
  <div class="tip" style="left:753px">
    <div class="img" style="background:linear-gradient(135deg,#dfe3e7,#a4b0bd 50%,#3d4b5c)" role="img" aria-label="Plumber installing a kitchen tap"></div>
    <div class="card">Case Study: Air conditioning<br>&amp; Furnace Installation</div>
    <a class="btn">Read More</a>
  </div>
</section>

<!-- cta -->
<section class="abs cta" role="img" aria-label="Friendly plumber in a blue cap and work uniform">
  <h2>Get Us To Your Front Door Today</h2>
  <p>Taps plumber services is the trusted name in heating, cooling, and plumbing services.<br>Contact us by filling out the form below – comfort is only a click away!</p>
  <a class="btn">Request Service Today</a>
</section>

<!-- footer -->
<svg class="abs footer-shape" width="1200" height="474" viewBox="0 0 1200 474"><path d="M0 130C180 60 330 20 520 50C640 68 700 110 840 80C950 58 1080 10 1200 0V474H0z" fill="#1f3a5f"/></svg>
<footer class="footer">
  <svg class="abs" style="left:156px;top:3852px" width="20" height="28" viewBox="0 0 12 16"><path d="M6 .8a5.2 5.2 0 0 0-5.2 5.2C.8 10 6 15 6 15s5.2-5 5.2-9A5.2 5.2 0 0 0 6 .8zm0 7.4A2.2 2.2 0 1 1 6 3.8a2.2 2.2 0 0 1 0 4.4z" fill="none" stroke="#fff" stroke-width="1.2"/></svg>
  <div class="addr" style="left:203px"><b>PLUMBER SERVICES</b>48 Harbour Rd. Eastvale, NSW 2140<div class="tel">☎ 000-000-0000 &nbsp; ⎙ 000-000-0000</div></div>
  <svg class="abs" style="left:440px;top:3852px" width="20" height="28" viewBox="0 0 12 16"><path d="M6 .8a5.2 5.2 0 0 0-5.2 5.2C.8 10 6 15 6 15s5.2-5 5.2-9A5.2 5.2 0 0 0 6 .8zm0 7.4A2.2 2.2 0 1 1 6 3.8a2.2 2.2 0 0 1 0 4.4z" fill="none" stroke="#fff" stroke-width="1.2"/></svg>
  <div class="addr" style="left:488px"><b>PLUMBER SERVICES</b>12 Creek St. Suite 4 Milton, QLD 4064<div class="tel">☎ 000-000-0000 &nbsp; ⎙ 000-000-0000</div></div>
  <div class="fsocial"><span></span><span></span><span></span><span></span></div>
  <div class="abs badge"></div>

  <div class="fcol" style="left:161px"><h4>Quick Links</h4>Air Conditioning<br>Heating<br>Plumbing<br>Water Treatment<br>Contact Us</div>
  <div class="fcol small" style="left:378px"><h4>Quick Links</h4>SERVICES<br>BILLING<br>CAREERS<br>BLOG<br>CONTACT</div>
  <div class="news">
    <h4>Subscribe The Newsletter</h4>
    <p>Subscribe to our newsletter and stay updated on the latest news. We will keep you informed about special offers.</p>
    <div class="form"><div class="input">Email Address*</div><div class="submit">Submit</div></div>
  </div>
  <div class="abs copy">©2018 BY PLUMBER SERVICES. ALL RIGHTS RESERVED.</div>
</footer>

</body>
</html>
```